Software engineering company needs business card

I need a cool business card. Company: Byte Merano Larchwood Ave 41 58213 Dunmere Name: Gerald Hofmann CEO / Managing Director & Owner

Industry/Entity Type

Business

```html
<!DOCTYPE html>
<html lang="de">
<head>
<meta charset="utf-8">
<title>Byte Merano – Business Card</title>
<link href="https://fonts.googleapis.com/css2?family=Open+Sans:wght@400;600;700&display=swap" rel="stylesheet">
<style>
  :root {
    --backdrop: #0c0c0c;
    --card: #242424;
    --green: #78bb2c;
    --grey: #8d8d8d;
    --grey-strong: #a3a3a3;
  }
  * { margin: 0; padding: 0; box-sizing: border-box; }
  html, body {
    width: 1200px; height: 727px; overflow: hidden;
    background: var(--backdrop);
    font-family: "Open Sans", sans-serif;
  }
  .card {
    position: absolute; left: 130px; top: 68px;
    width: 940px; height: 590px;
    background: var(--card);
    border-radius: 4px;
  }
  .identity {
    position: absolute; left: 62px; top: 78px;
    padding-left: 26px;
  }
  .identity__bar {
    position: absolute; left: 0; top: 6px;
    width: 13px; height: 74px;
    background: var(--green);
  }
  .identity__name {
    font-size: 36px; line-height: 44px;
    color: var(--grey); font-weight: 400;
  }
  .identity__name strong { font-weight: 700; color: var(--grey-strong); }
  .identity__role {
    font-size: 24px; line-height: 30px;
    color: var(--green); font-weight: 400;
  }
  .contact {
    position: absolute; left: 150px; top: 372px;
    list-style: none;
  }
  .contact__item {
    display: flex; align-items: flex-start; gap: 18px;
    font-size: 24px; line-height: 30px; color: var(--grey);
    margin-bottom: 18px;
  }
  .contact__icon { width: 26px; height: 26px; flex: none; margin-top: 3px; fill: var(--green); }
  .brand {
    position: absolute; right: 70px; top: 300px;
    display: flex; align-items: center; gap: 18px;
  }
  .brand__mark { width: 30px; height: 30px; background: var(--green); }
  .brand__name {
    font-size: 54px; font-weight: 600; letter-spacing: 1px;
    color: var(--green);
  }
</style>
</head>
<body>
  <article class="card">
    <header class="identity">
      <span class="identity__bar"></span>
      <h1 class="identity__name">Gerald <strong>Hofmann</strong></h1>
      <p class="identity__role">CEO / Geschäftsführer &amp; Inhaber</p>
    </header>

    <div class="brand">
      <span class="brand__mark"></span>
      <span class="brand__name">Byte Merano</span>
    </div>

    <ul class="contact">
      <li class="contact__item">
        <svg class="contact__icon" viewBox="0 0 24 24" aria-hidden="true"><path d="M12 2a7 7 0 0 0-7 7c0 5 7 13 7 13s7-8 7-13a7 7 0 0 0-7-7zm0 9.5A2.5 2.5 0 1 1 12 6.5a2.5 2.5 0 0 1 0 5z"/></svg>
        <span>Larchwood Ave 41<br>58213 Dunmere</span>
      </li>
      <li class="contact__item">
        <svg class="contact__icon" viewBox="0 0 24 24" aria-hidden="true"><path d="M3 7c0-2 4-3 9-3s9 1 9 3v2h-5V7.5c-1-.4-2.5-.6-4-.6s-3 .2-4 .6V9H3zM6 10h12l3 9H3zm6 2.5a2.5 2.5 0 1 0 0 5 2.5 2.5 0 0 0 0-5z"/></svg>
        <span>000 000 0000</span>
      </li>
      <li class="contact__item">
        <svg class="contact__icon" viewBox="0 0 24 24" aria-hidden="true"><path d="M2 5h20v14H2zm2 2v.5l8 6 8-6V7zm0 3v7h16v-7l-8 6z"/></svg>
        <span>office@bytemerano.com</span>
      </li>
    </ul>
  </article>
</body>
</html>
```